Brookfield Animal Care Partners of Central Pennsylvania

I need a business card design for a new company in Harrisburg PA called "Animal Care Partners of Brookfield Central PA". I will be providing relief services for veterinarians who need coverage during vacations; sick/maternity leave, etc. I would like to see the veterinarian symbol incorporated in the design in combination with animals (dogs /cats/birds/reptiles an pocket pets). Include My full name: Tomás R. Quintela DVM, MLAS, BS. Also include my e mail (dvmtrq@mailnest.example) and phone number 5550184627

Target Market(s)

Small Animal Veterinarian, practice owner

Industry/Entity Type

Business

Contact Information for Business Card

Brookfield Animal Care Partners of Central PA

Font styles to use
Script

Requirements
Must have
• Veterinarian caduceus (see image) and Small animals (pets) within the logo.
Nice to have
• Give a sense of relaxation (vacationing)
Should not have
• Large animals, i.e. horses, cows, zoo animals...

```html
<!DOCTYPE html>
<html lang="en">
<head>
<meta charset="utf-8">
<title>Animal Care Partners of Brookfield Central PA — Business Card</title>
<link rel="stylesheet" href="https://fonts.googleapis.com/css2?family=Kaushan+Script&family=Cormorant+SC:wght@400;500&display=swap">
<style>
  :root {
    --backdrop: #e9e6e1;
    --card-white: #ffffff;
    --card-orange: #f0913a;
    --leaf-green: #7cc242;
    --title-green: #5aa82c;
    --ink-white: #ffffff;
    --pet-tan: #c99a6e;
    --pet-brown: #8a6b55;
    --pet-dark: #3a3230;
    --pet-light: #d9c6b4;
  }
  * { margin: 0; padding: 0; box-sizing: border-box; }
  html, body {
    width: 1200px; height: 799px; overflow: hidden;
    background: var(--backdrop);
  }
  .stage {
    width: 1200px; height: 799px;
    display: flex; align-items: center; justify-content: center;
  }
  .business-card {
    position: relative;
    width: 1050px; height: 600px;
    background: var(--card-white);
    overflow: hidden;
    box-shadow: 0 10px 30px rgba(0,0,0,0.15);
  }
  .card-title {
    position: absolute; left: 50px; top: 32px; width: 950px;
    font-family: "Kaushan Script", cursive;
    font-size: 48px; color: var(--title-green);
    text-align: center; white-space: nowrap;
  }
  .title-rule {
    position: absolute; left: 170px; top: 116px;
    width: 680px; height: 4px; background: var(--leaf-green);
  }
  .orange-band {
    position: absolute; left: 0; top: 178px; right: 0; bottom: 0;
    background: var(--card-orange);
    border-top: 5px solid var(--leaf-green);
  }
  .pet-photo {
    position: absolute; left: 40px; top: 150px;
    width: 520px; height: 420px;
    border-radius: 10px;
    background: linear-gradient(100deg, var(--pet-brown) 0%, var(--pet-light) 22%, var(--pet-tan) 45%, var(--pet-dark) 70%, var(--pet-tan) 100%);
  }
  .brand-badge {
    position: absolute; left: 560px; top: 130px;
    width: 200px; height: 200px; border-radius: 50%;
    background: var(--card-orange);
    border: 6px solid var(--card-white);
    box-shadow: 0 0 0 4px var(--leaf-green);
    display: flex; align-items: center; justify-content: center;
    text-align: center;
  }
  .brand-badge span {
    font-family: "Cormorant SC", serif; font-weight: 500;
    font-size: 24px; line-height: 1.1; color: var(--ink-white);
    padding: 0 22px;
  }
  .contact-block {
    position: absolute; left: 705px; top: 350px; width: 320px;
    font-family: "Cormorant SC", serif; color: var(--ink-white);
  }
  .person-name { font-size: 32px; font-weight: 500; line-height: 1; white-space: nowrap; }
  .person-degrees { font-size: 20px; margin-top: 8px; text-align: right; padding-right: 20px; }
  .contact-list { list-style: none; margin-top: 60px; }
  .contact-list li {
    display: flex; align-items: center; gap: 10px;
    font-size: 24px; line-height: 1.6; white-space: nowrap;
  }
  .contact-list svg { width: 22px; height: 22px; flex: none; }
  .contact-email { font-size: 21px; }
</style>
</head>
<body>
<main class="stage">
  <article class="business-card">
    <div class="orange-band"></div>
    <h1 class="card-title">Animal Care Partners of Brookfield Central PA</h1>
    <div class="title-rule"></div>
    <div class="pet-photo" role="img" aria-label="Group photo of pets: a large dog, a parrot, cats, kittens, a ferret, a small bird and a tortoise"></div>
    <div class="brand-badge"><span>Brookfield Animal Care Partners</span></div>
    <section class="contact-block">
      <p class="person-name">Tomás R. Quintela</p>
      <p class="person-degrees">DVM, MLAS, BS</p>
      <ul class="contact-list">
        <li>
          <svg viewBox="0 0 24 24" aria-hidden="true" fill="var(--leaf-green)">
            <ellipse cx="12" cy="16" rx="6" ry="5"/>
            <circle cx="5" cy="9" r="2.4"/><circle cx="9.5" cy="5" r="2.4"/>
            <circle cx="14.5" cy="5" r="2.4"/><circle cx="19" cy="9" r="2.4"/>
          </svg>
          <span>555 018 4627</span>
        </li>
        <li>
          <svg viewBox="0 0 24 24" aria-hidden="true" fill="var(--leaf-green)">
            <ellipse cx="12" cy="16" rx="6" ry="5"/>
            <circle cx="5" cy="9" r="2.4"/><circle cx="9.5" cy="5" r="2.4"/>
            <circle cx="14.5" cy="5" r="2.4"/><circle cx="19" cy="9" r="2.4"/>
          </svg>
          <span class="contact-email">dvmtrq@mailnest.example</span>
        </li>
      </ul>
    </section>
  </article>
</main>
</body>
</html>
```